Create a landing page for a new product market combination for an international software company

We are a software company being in the BtoB market for over 20 years. Our product is a software tool that allows for very flexible and versatile cost calculations for companies. We sell to all industries in over 40 countries with 500 clients. We have fairly recently seen a succesfull "competitor" (www.quorvel.com) come up in the niche market of IT costing. This competitor has launched an independent platform with regards to managing IT costs (www.PLXguild.org). In this independent platform standards are set, events are organised and books are written. Since our software can handle all type of costing questions we can en already do play a role in IT costing. We have therefore become a sponsor of the PLX guild. Besides that we came accross the opportunity to buy the URL: www.plxsoftware.com Which we did. We are now looking for a design on that landing page that communicates the fact that the visitor has landed with a company that have in depth knowledge on the PLX subject and provide an effective an affordable tooling for PLX. Currently the difference between the professionalism of our own website (www.brandivex.com) and that of the competitor (www.quorvel.com) and the independent council (www.plxguild.org). is too big.

Target Market(s)

BtB with large IT spend

Number of Pages Required

1 page

Colors

Designer to choose colors to be used in the design.

Requirements
Must have
• A proffessional look and feel
Should not have
• Definetely not too much information and wording

```html
<!DOCTYPE html>
<html lang="en">
<head>
<meta charset="utf-8">
<title>PLX Software – Technology Business Management</title>
<link rel="stylesheet" href="https://fonts.googleapis.com/css2?family=Poppins:wght@300;400;500;600;700&display=swap">
<style>
:root{
  --navy:#0c2440;
  --navy-deep:#0a1b30;
  --blue:#17406b;
  --orange:#f26522;
  --sky:#1aa3e0;
  --ink:#222831;
  --muted:#7a7f87;
  --line:#d9dde2;
  --footer:#4a4e53;
  --footer-deep:#3a3d41;
  --white:#ffffff;
}
*{box-sizing:border-box;margin:0;padding:0}
html,body{width:676px;height:1200px;overflow:hidden}
body{font-family:"Poppins",sans-serif;color:var(--ink);background:var(--white);position:relative}
svg{display:block}
.abs{position:absolute}
.topbar{top:0;left:0;width:676px;height:14px;background:var(--navy-deep);color:#c9d2dc;font-size:4.6px;line-height:14px;padding-left:130px}
.flags{position:absolute;right:130px;top:3px;display:flex;gap:3px}
.flag{width:11px;height:8px;display:flex;flex-direction:column;overflow:hidden}
.flag.it{flex-direction:row}
.flag span{flex:1}
.nav{top:14px;left:0;width:676px;height:30px;background:var(--white)}
.brand{position:absolute;left:130px;top:8px;font-size:11px;font-weight:500;color:var(--navy);letter-spacing:.2px;line-height:14px}
.menu{position:absolute;left:332px;top:0;height:30px;display:flex;align-items:center;gap:9px;font-size:5.8px;font-weight:500;color:var(--ink)}
.btn-join{position:absolute;left:514px;top:9px;width:32px;height:12px;background:var(--orange);color:#fff;font-size:4.6px;font-weight:600;text-align:center;line-height:12px;border-radius:1px}
.hero{top:44px;left:0;width:676px;height:182px;background:linear-gradient(90deg,#17304f 0%,#1f4670 60%,#2a5680 100%)}
.hero h1{position:absolute;left:130px;top:40px;font-size:21px;line-height:23.5px;font-weight:700;color:#fff}
.hero p{position:absolute;left:130px;top:94px;font-size:11px;font-weight:300;color:#fff}
.btn-orange{position:absolute;background:var(--orange);color:#fff;font-weight:600;text-align:center;border-radius:1px;text-transform:uppercase}
.sec-title{position:absolute;left:0;width:676px;text-align:center;font-size:12px;font-weight:400}
.convo{top:226px;left:0;width:676px;height:202px;background:var(--navy)}
.card{position:absolute;top:48px;width:96px;height:132px;background:#fff;text-align:center;border-radius:1px}
.card svg{margin:11px auto 0}
.card h3{font-size:7.6px;font-weight:500;line-height:10.5px;margin-top:13px;color:var(--ink)}
.card p{font-size:5px;line-height:9px;color:var(--muted);margin:5px 12px 0}
.culture{top:428px;left:0;width:676px;height:186px;background:linear-gradient(180deg,#d8d8d8 0%,#f6f6f6 50%,#dcdcdc 100%)}
.feature{position:absolute;top:46px;width:220px;text-align:center}
.feature svg{margin:0 auto}
.feature h3{font-size:7.6px;font-weight:500;margin-top:9px}
.feature p{font-size:5px;line-height:9px;color:var(--muted);margin:5px 22px 0}
.btn-ghost{display:inline-block;margin-top:6px;width:39px;height:13px;line-height:12px;border:1px solid var(--line);background:#fff;font-size:4.4px;border-radius:1px;box-shadow:0 1px 1px rgba(0,0,0,.08)}
.pillars{top:614px;left:0;width:676px;height:218px;background:radial-gradient(circle at 30% 40%,#1d4a78 0%,#143a62 55%,#0f2f52 100%);color:#fff}
.pillar{position:absolute;top:50px;width:96px;text-align:center}
.pillar svg{margin:0 auto}
.pillar h3{font-size:7.6px;font-weight:500;line-height:10.5px;margin-top:11px}
.pillar p{font-size:5.1px;line-height:9.2px;margin:5px 2px 0}
.news{top:832px;left:0;width:676px;height:220px;background:linear-gradient(180deg,#f5f5f5,#e8e8e8)}
.post{position:absolute;top:36px;width:203px;height:162px;background:#fff;box-shadow:0 0 2px rgba(0,0,0,.1)}
.post .photo{position:absolute;left:10px;top:10px;width:183px;height:78px}
.tag{position:absolute;left:13px;top:100px;display:flex;height:10px}
.tag b{width:12px;background:#4a4e53}
.tag span{background:var(--sky);color:#fff;font-size:4px;line-height:10px;padding:0 6px;font-weight:500}
.post h4{position:absolute;left:13px;top:117px;font-size:7.6px;font-weight:500}
.post p{position:absolute;left:13px;top:131px;width:180px;font-size:4.6px;line-height:7.2px;color:var(--muted)}
.cta{top:1052px;left:0;width:676px;height:62px;background:#fff}
.cta h2{position:absolute;left:195px;top:18px;font-size:12px;font-weight:400}
.cta p{position:absolute;left:195px;top:36px;font-size:5px;color:var(--muted)}
.btn-sky{position:absolute;left:425px;top:22px;width:56px;height:20px;background:var(--sky);color:#fff;font-size:4.6px;font-weight:600;text-align:center;line-height:20px;border-radius:1px}
.footer{top:1114px;left:0;width:676px;height:71px;background:var(--footer);color:#d0d3d7}
.fcol{position:absolute;top:14px}
.fcol h5{font-size:5.4px;font-weight:500;color:#fff;margin-bottom:6px}
.fcol li{list-style:none;font-size:3.8px;line-height:7px;text-transform:uppercase}
.legal{top:1185px;left:0;width:676px;height:15px;background:var(--footer-deep);color:#b7bbc0;font-size:3.8px;text-align:center;line-height:15px}
</style>
</head>
<body>

<div class="abs topbar">Helpdesk: +31 (0)20 555 0142 &nbsp;|&nbsp; Fax: +31 (0)20 555 0178
  <div class="flags">
    <div class="flag"><span style="background:#ae1c28"></span><span style="background:#fff"></span><span style="background:#21468b"></span></div>
    <div class="flag it"><span style="background:#009246"></span><span style="background:#fff"></span><span style="background:#ce2b37"></span></div>
    <div class="flag"><span style="background:#1f3c8c"></span></div>
  </div>
</div>

<header class="abs nav">
  <div class="brand">PLX Software</div>
  <nav class="menu"><span>Who We Are</span><span>Learn PLX</span><span>Awards</span><span>Events</span><span>Emerge</span></nav>
  <div class="btn-join">JOIN US</div>
</header>

<section class="abs hero" role="img" aria-label="Business team in a meeting room, under a dark blue overlay">
  <h1>Technology Business<br>Management</h1>
  <p>Effective and affordable</p>
  <div class="btn-orange" style="left:130px;top:124px;width:51px;height:16px;font-size:4.6px;line-height:16px">Know More</div>
</section>

<section class="abs convo">
  <h2 class="sec-title" style="top:19px;color:#fff">Enable The Right Business Conversations</h2>
  <div class="card" style="left:130px">
    <svg width="38" height="38" viewBox="0 0 38 38"><circle cx="19" cy="19" r="16" fill="none" stroke="var(--orange)" stroke-width="3" stroke-dasharray="80 21" transform="rotate(120 19 19)"/><circle cx="19" cy="19" r="3" fill="var(--orange)"/><path d="M19 19 L28 10" stroke="var(--orange)" stroke-width="3" stroke-linecap="round"/><path d="M9 19h3M19 9v3M26 19h3" stroke="var(--orange)" stroke-width="2"/></svg>
    <h3>Cost Of<br>Performance</h3>
    <p>Deliver technology, services, and projects efficiently to the business.</p>
  </div>
  <div class="card" style="left:237px">
    <svg width="38" height="38" viewBox="0 0 38 38"><rect x="10" y="2" width="18" height="34" fill="var(--orange)"/><g fill="#fff"><rect x="13" y="6" width="3" height="3"/><rect x="18" y="6" width="3" height="3"/><rect x="23" y="6" width="2" height="3"/><rect x="13" y="12" width="3" height="3"/><rect x="18" y="12" width="3" height="3"/><rect x="23" y="12" width="2" height="3"/><rect x="13" y="18" width="3" height="3"/><rect x="18" y="18" width="3" height="3"/><rect x="23" y="18" width="2" height="3"/><rect x="16" y="28" width="6" height="8"/></g></svg>
    <h3>Business-Aligned<br>Portfolio</h3>
    <p>Optimize portfolios to deliver the most value for the level of spending.</p>
  </div>
  <div class="card" style="left:343px">
    <svg width="38" height="38" viewBox="0 0 38 38"><circle cx="19" cy="16" r="10" fill="var(--orange)"/><rect x="15" y="25" width="8" height="6" fill="var(--orange)"/><path d="M20 9l-5 8h4l-2 6 6-9h-4z" fill="#fff"/><path d="M4 16h3M31 16h3M8 5l2 2M30 5l-2 2" stroke="var(--orange)" stroke-width="2"/></svg>
    <h3>Investment In<br>Innovation</h3>
    <p>Allocate adequate resources on new and enhanced services and on business innovation.</p>
  </div>
  <div class="card" style="left:450px">
    <svg width="38" height="38" viewBox="0 0 38 38"><circle cx="19" cy="19" r="16" fill="var(--orange)"/><path d="M14 14l5-4 5 4-2 6h-6z M19 10V3 M24 14l9-2 M14 14l-9-2 M22 20l5 8 M16 20l-5 8" stroke="#fff" stroke-width="2" fill="none"/></svg>
    <h3>Enterprise<br>Agility</h3>
    <p>Help the business respond quickly to market opportunities or threats.</p>
  </div>
</section>

<section class="abs culture">
  <h2 class="sec-title" style="top:20px">Foster a Business Culture in IT</h2>
  <div class="feature" style="left:121px">
    <svg width="64" height="50" viewBox="0 0 64 50"><circle cx="14" cy="18" r="7" fill="var(--orange)"/><path d="M2 44c0-11 5-16 12-16s12 5 12 16z" fill="var(--orange)"/><circle cx="50" cy="18" r="7" fill="var(--orange)"/><path d="M38 44c0-11 5-16 12-16s12 5 12 16z" fill="var(--orange)"/><circle cx="32" cy="11" r="9" fill="var(--navy)"/><path d="M16 48c0-15 7-22 16-22s16 7 16 22z" fill="var(--navy)"/><path d="M29 26l3 3 3-3-2 18h-2z" fill="#fff"/></svg>
    <h3>Position for Value</h3>
    <p>Define what you deliver in terms of business capabilities that are understood and valued by your business unit partners, so you can work together to improve business outcomes.</p>
    <span class="btn-ghost">Read More</span>
  </div>
  <div class="feature" style="left:335px">
    <svg width="64" height="50" viewBox="0 0 64 50"><g fill="var(--navy)"><rect x="4" y="30" width="7" height="20"/><rect x="19" y="22" width="7" height="28"/><rect x="34" y="26" width="7" height="24"/><rect x="49" y="16" width="7" height="34"/></g><polyline points="7,20 22,10 37,16 53,4" fill="none" stroke="var(--orange)" stroke-width="2.5"/><g fill="var(--orange)"><circle cx="7" cy="20" r="3"/><circle cx="22" cy="10" r="3"/><circle cx="37" cy="16" r="3"/><circle cx="53" cy="4" r="3"/></g></svg>
    <h3>Continuously Improve</h3>
    <p>Execute a strategic roadmap for PLX maturity by integrating PLX into your day-to-day processes and thinking, so that PLX drives every value conversation with your peers</p>
    <span class="btn-ghost">Read More</span>
  </div>
</section>

<section class="abs pillars">
  <h2 class="sec-title" style="top:17px;color:#fff">Enable The Right Business Conversations</h2>
  <div class="pillar" style="left:130px">
    <svg width="38" height="38" viewBox="0 0 38 38"><rect x="1" y="1" width="36" height="36" fill="none" stroke="#fff" stroke-width="2"/><path d="M7 19c4-6 8-8 12-8s8 2 12 8c-4 6-8 8-12 8s-8-2-12-8z" fill="#fff"/><circle cx="19" cy="19" r="5" fill="var(--blue)"/><circle cx="19" cy="19" r="2.2" fill="#fff"/></svg>
    <h3>Create<br>Transparency</h3>
    <p>Translate your spending, consumption, and capacity into meaningful perspectives for technology and business decision-makers.</p>
  </div>
  <div class="pillar" style="left:237px">
    <svg width="38" height="38" viewBox="0 0 38 38"><rect x="1" y="1" width="36" height="36" fill="none" stroke="#fff" stroke-width="2"/><g fill="#fff"><rect x="9" y="22" width="3" height="8"/><rect x="14" y="18" width="3" height="12"/><rect x="19" y="20" width="3" height="10"/><rect x="24" y="15" width="3" height="15"/></g><polyline points="9,17 15,12 20,15 29,8" fill="none" stroke="#fff" stroke-width="1.6"/></svg>
    <h3>Shape<br>Business Demand</h3>
    <p>Communicate costs and consumption to business units to drive informed trade-off decisions and better consumption behavior.</p>
  </div>
  <div class="pillar" style="left:343px">
    <svg width="38" height="38" viewBox="0 0 38 38"><rect x="1" y="1" width="36" height="36" fill="none" stroke="#fff" stroke-width="2"/><text x="19" y="27" text-anchor="middle" font-family="Poppins,sans-serif" font-weight="700" font-size="22" fill="#fff">$</text></svg>
    <h3>Deliver Value<br>For Money</h3>
    <p>Maximize value and demonstrate industry-comparable cost-effectiveness for services and innovation you provide.</p>
  </div>
  <div class="pillar" style="left:452px">
    <svg width="38" height="38" viewBox="0 0 38 38"><rect x="1" y="1" width="36" height="36" fill="none" stroke="#fff" stroke-width="2"/><g stroke="#fff" stroke-width="1.8" fill="none"><path d="M7 7l4 4M11 7l-4 4M27 17l4 4M31 17l-4 4"/><circle cx="22" cy="29" r="3"/><path d="M9 30c0-10 6-16 16-18"/><path d="M21 9l4 3-3 4"/></g></svg>
    <h3>Plan &amp;<br>Govern</h3>
    <p>Collaborate to align your annual budget and resource plans to strategic business priorities and manage to the plan.</p>
  </div>
  <div class="btn-orange" style="left:319px;top:182px;width:39px;height:14px;font-size:4.4px;line-height:14px;text-transform:none">Know More</div>
</section>

<section class="abs news">
  <h2 class="sec-title" style="top:13px">News</h2>
  <article class="post" style="left:130px">
    <div class="photo" role="img" aria-label="Photo of two colleagues talking in an office with sticky notes on a board" style="background:linear-gradient(120deg,#2c3036 0%,#5b5f66 45%,#c9c6c2 100%)"></div>
    <div class="tag"><b></b><span>27 Feb 19</span></div>
    <h4>Brandivex PLX Cost model</h4>
    <p>Define what you deliver in terms of business capabilities that are understood and valued by your business unit partners, so you can work together to improve business outcomes.[...]</p>
  </article>
  <article class="post" style="left:343px">
    <div class="photo" role="img" aria-label="Photo of a group of colleagues gathered around a laptop at a table" style="background:linear-gradient(120deg,#d7d3cc 0%,#a9a39b 50%,#5e5852 100%)"></div>
    <div class="tag"><b></b><span>27 Feb 19</span></div>
    <h4>Cost Management Training Course Vietnam</h4>
    <p>Define what you deliver in terms of business capabilities that are understood and valued by your business unit partners, so you can work together to improve business outcomes.[...]</p>
  </article>
</section>

<section class="abs cta">
  <h2>Join the most happening community</h2>
  <p>Lorem Ipsum is simply dummy text of the printing and typesetting industry.</p>
  <div class="btn-sky">JOIN NOW</div>
</section>

<footer class="abs footer">
  <div class="fcol" style="left:130px"><h5>Product</h5><ul><li>Overview</li><li>Details</li><li>Functions</li><li>Screenshots</li></ul></div>
  <div class="fcol" style="left:186px"><h5>Markets</h5><ul><li>Healthcare</li><li>City Councils</li><li>Banks</li><li>Telecom</li></ul></div>
  <div class="fcol" style="left:244px"><h5>Partner</h5><ul><li>Dedicated Partners</li><li>Independent Consulting</li><li>Affiliates</li></ul></div>
  <div class="fcol" style="left:312px"><h5>Support</h5><ul><li>Downloads</li><li>Licenses</li><li>Known Issues</li></ul></div>
  <div class="fcol" style="left:378px"><h5>Contact Netherlands</h5><ul><li>Tel: +31 (0)20 555 0131</li><li>Helpdesk: +31 (0)20 555 0142</li><li>Fax: +31 (0)20 555 0178</li></ul></div>
  <div class="fcol" style="left:466px"><h5>Contact USA</h5><ul><li>Tel: +1 480 555 0163</li><li>Helpdesk: +31 (0)20 555 0142</li><li>Fax: +31 (0)20 555 0178</li></ul></div>
</footer>
<div class="abs legal">© NORVANE COSTING BV 2019 | PRIVACY POLICY | TERMS OF USE</div>

</body>
</html>
```